Website art for a private investigator.

The purposed graphic is for a business website ( corvashield.example ). The business name is “Halberd & Associates ltd.” This firm is a private investigation agency. The purposed graphic will be placed in the upper most main area of the main page of the website. If you look at the website now there is no graphic.

I have an idea of what I am looking for. I imagine a graphic depicting a contemporary private investigator walking through a dark alley searching for some unknown item. This is symbolic of private investigators hired to find information for people who their selfs do not have the know how nor could they handle the complexity and high stress environment. When I say contemporary I am referring to todays private investigators typically highly educated and well dressed.

Target Market(s)

People who need a private investigator

Industry/Entity Type

Business

Requirements
Must have
• match website; I have an idea of what I am looking for. I imagine a graphic depicting a contemporary private investigator walking through a dark alley searching for some unknown item. This is symbolic of private investigators hired to find information for people who their selfs do not have the know how nor could they handle the complexity and high stress environment. When I say contemporary I am referring to todays private investigators typically highly educated and well dressed.
Should not have
• Everyone please understand, I am not looking for a new website. I am only looking for the image. If you have submitted a design and its displayed on another website other than mine. I will not select your design. I am sorry for being harsh, but I asked for the image to match my website.

```html
<!DOCTYPE html>
<html lang="en">
<head>
<meta charset="utf-8">
<title>Halberd &amp; Associates Ltd</title>
<link rel="stylesheet" href="https://fonts.googleapis.com/css2?family=Cinzel:wght@400;600&family=Libre+Baskerville&family=Lato:ital,wght@0,700;1,400&family=Montserrat:wght@400&display=swap">
<style>
  :root {
    --page: #ffffff;
    --ink: #2b2b2b;
    --ink-soft: #1f1f1f;
    --social-bar: #000000;
    --dark-panel: #141519;
    --hero-light: #c9ccd3;
    --hero-mid: #6d717b;
    --hero-dark: #2a2c32;
    --accent-blue: #7d9ed6;
    --brand-grey: #8a8d93;
    --logo-grey: #8c9099;
    --quote-grey: #c8c8c8;
    --button-top: #4a8fd6;
    --button-bottom: #2462ac;
  }
  * { box-sizing: border-box; margin: 0; padding: 0; }
  html, body { width: 1200px; height: 900px; overflow: hidden; background: var(--page); }
  .page { position: relative; width: 1200px; height: 900px; background: var(--page); }

  .hero { position: absolute; left: 0; top: 0; width: 1200px; height: 291px; overflow: hidden; }
  .hero-photo {
    position: absolute; left: 0; top: 0; width: 886px; height: 291px;
    background:
      radial-gradient(ellipse 280px 200px at 600px 130px, var(--hero-dark) 0%, transparent 70%),
      radial-gradient(ellipse 300px 220px at 150px 180px, var(--hero-light) 0%, transparent 75%),
      linear-gradient(90deg, var(--hero-light) 0%, var(--hero-mid) 45%, var(--hero-dark) 100%);
  }
  .hero-panel { position: absolute; left: 886px; top: 0; width: 314px; height: 291px; background: var(--dark-panel); }

  .social-bar {
    position: absolute; left: 0; top: 0; width: 420px; height: 64px;
    background: var(--social-bar);
    display: flex; align-items: center; justify-content: space-around; padding: 0 20px;
  }
  .social-dot { width: 20px; height: 20px; border-radius: 50%; background: #ffffff; }

  .main-nav {
    position: absolute; left: 462px; top: 22px; display: flex; gap: 42px;
    font-family: "Lato", sans-serif; font-weight: 700; font-size: 13px; color: #ffffff;
  }

  .slogan {
    position: absolute; top: 137px; font-family: "Cinzel", serif; font-size: 26px; color: #ffffff; letter-spacing: 0.5px;
  }
  .slogan-left { left: 463px; }
  .slogan-left .accent { color: var(--accent-blue); font-weight: 600; }
  .slogan-right { right: 30px; }

  .logo-mark {
    position: absolute; left: 35px; top: 176px; width: 90px; height: 90px;
    border: 3px solid var(--logo-grey); border-radius: 50%;
    display: flex; align-items: center; justify-content: center;
    font-family: "Libre Baskerville", serif; font-size: 22px; color: var(--logo-grey);
  }

  .brand { position: absolute; right: 30px; text-align: right; font-family: "Libre Baskerville", serif; }
  .brand-name { top: 290px; top: 290px; }
  .brand .name { position: absolute; right: 0; top: -0px; }
  .brand-title { position: absolute; right: 30px; top: 290px; top: 290px; }
  .company-name {
    position: absolute; right: 30px; top: 292px; top: 291px;
  }
  .hero-brand { position: absolute; right: 30px; top: 290px; }
  .hero-company { position: absolute; right: 30px; top: 291px; }
  .company { position: absolute; right: 30px; top: 290px; }

  .firm-name {
    position: absolute; right: 30px; top: 221px;
    font-family: "Libre Baskerville", serif; font-size: 19px; color: var(--brand-grey);
  }
  .firm-tagline {
    position: absolute; right: 30px; top: 252px;
    font-family: "Libre Baskerville", serif; font-size: 12px; color: #ffffff;
  }

  .contact-phone {
    position: absolute; left: 727px; top: 321px;
    font-family: "Montserrat", sans-serif; font-size: 21px; color: var(--ink);
  }
  .request-button {
    position: absolute; left: 735px; top: 372px; width: 215px; height: 36px;
    border-radius: 18px; background: linear-gradient(180deg, var(--button-top), var(--button-bottom));
    box-shadow: 0 1px 2px rgba(0,0,0,0.3);
    font-family: "Lato", sans-serif; font-weight: 700; font-size: 13px; color: #ffffff;
    display: flex; align-items: center; justify-content: center;
  }

  .section-title {
    position: absolute; left: 93px; top: 474px;
    font-family: "Montserrat", sans-serif; font-size: 26px; color: var(--ink);
  }
  .quote-mark {
    position: absolute; font-family: "Lato", sans-serif; font-style: italic; font-size: 64px; line-height: 1;
    color: var(--quote-grey);
  }
  .quote-open-1 { left: 98px; top: 540px; }
  .quote-close-1 { left: 1016px; top: 660px; }
  .quote-open-2 { left: 98px; top: 720px; }
  .intro-text {
    position: absolute; left: 101px; top: 577px; width: 990px;
    font-family: "Lato", sans-serif; font-style: italic; font-size: 15.5px; line-height: 27.5px; color: var(--ink-soft);
  }
</style>
</head>
<body>
<div class="page">
  <header class="hero">
    <div class="hero-photo" role="img" aria-label="Close-up photograph of an ornate masquerade mask in cool grey tones"></div>
    <div class="hero-panel"></div>

    <nav class="social-bar" aria-label="Social links">
      <span class="social-dot"></span><span class="social-dot"></span><span class="social-dot"></span>
      <span class="social-dot"></span><span class="social-dot"></span><span class="social-dot"></span>
    </nav>

    <nav class="main-nav">
      <span>Main</span><span>Investigation &amp; Analysis</span><span>News</span><span>Fees</span>
    </nav>

    <p class="slogan slogan-left">Seeing <span class="accent">Beyond</span></p>
    <p class="slogan slogan-right">What the World Sees</p>

    <div class="logo-mark">Logo</div>

    <p class="firm-name">Halberd &amp; Associates Ltd</p>
    <p class="firm-tagline">A Private Investigation and Analysis Firm</p>
  </header>

  <p class="contact-phone">Tel. (555) 014-2736</p>
  <div class="request-button">Sudmit Request For Service</div>

  <h1 class="section-title">Ohio and West Virginia Private Investigators</h1>
  <span class="quote-mark quote-open-1">&ldquo;</span>
  <p class="intro-text">Our experience and unbiased approach is your greatest strength! If you are an attorney, company, or private individual with a legal need we will provide you with accurate, timely and unbiassed information that will help you make an informed decision, mitigate risk, and resolve problems.</p>
  <span class="quote-mark quote-close-1">&rdquo;</span>
  <span class="quote-mark quote-open-2">&ldquo;</span>
</div>
</body>
</html>
```